Services Brochure

We need an revised brochure for our 3 main services. I have uploaded our old Brochure for reference. We have 3 main services (Managed IT Services, Business VoIP, Business Internet). Below is some text we would like included in the brochure for each service section. In addition I have attached a "mock up" showing that we want IT Services on top, VoIP in the middle and Internet at the bottom. Please use your design experience to select images that would fit well. I also included an image of the phone we would like to use.
Text for Brochure:
Title/Header: Unleash the Power of Local IT Solutions
IT Services That Mean Business
Experience fanatical customer service with our affordable, full-service IT solutions. We’re 100% local, ensuring leading response times and personalized support—so you can focus on what you do best.
Talk More, Worry Less with Our Telephone Services
Say goodbye to overpriced equipment and hello to our free phone plan. Keep your number and enjoy unlimited local and long-distance calling. Tailor your phone system to your business needs and rest assured—our rates are always the lowest in town.
Highspeed Internet That Sets You Apart
Stay connected with blazing-fast speeds—from 1Gbps to 10Gbps, both up and down. Benefit from a static IP address and unbeatable prices, backed by 100% local support. Get the connectivity your business deserves at the best value in town.
Elevate your business with cutting-edge technology.
Sorry everyone the banner size is 81" high and 33" wide.

```html
<!DOCTYPE html>
<html lang="en">
<head>
<meta charset="utf-8">
<title>Norvix – Local IT Solutions Brochure</title>
<link href="https://fonts.googleapis.com/css2?family=Archivo:wght@700;800&family=Roboto+Condensed:wght@400;700&display=swap" rel="stylesheet">
<style>
  :root{
    --navy:#2b2f86;
    --navy-deep:#1f2366;
    --navy-soft:#4a4fa8;
    --tab-gray:#8c8c8c;
    --text:#333;
    --white:#fff;
    --page-bg:#e6e6e6;
    --head:"Archivo", Arial, sans-serif;
    --body:"Roboto Condensed", Arial Narrow, sans-serif;
  }
  *{box-sizing:border-box;margin:0;padding:0}
  html,body{width:1200px;height:1200px;overflow:hidden;background:var(--page-bg)}
  .brochure{position:absolute;left:229px;top:75px;width:742px;height:1050px;background:var(--white);overflow:hidden;font-family:var(--body);color:var(--text)}
  .abs{position:absolute}

  /* hero */
  .hero{left:0;top:0;width:742px;height:535px;background:linear-gradient(90deg,var(--navy) 0%,#3b3f95 45%,#5a5fae 100%)}
  .hero-photo{left:250px;top:0;width:492px;height:535px;background:
      radial-gradient(ellipse at 75% 35%,rgba(230,225,235,.55),rgba(120,125,190,0) 55%),
      radial-gradient(ellipse at 40% 30%,rgba(200,200,225,.35),rgba(0,0,0,0) 50%),
      linear-gradient(90deg,rgba(43,47,134,0),rgba(150,155,205,.4))}
  .title-panel{left:0;top:29px;width:471px;height:121px;background:rgba(255,255,255,.93)}
  .title{left:30px;top:40px;font-family:var(--head);font-weight:800;color:var(--navy);line-height:1}
  .title .big{font-size:37px;display:block;letter-spacing:.3px}
  .title .mid{font-size:22px;display:block;margin:6px 0 5px}
  .brand{left:350px;top:30px;font-family:var(--head);font-weight:800;font-size:44px;color:var(--navy);letter-spacing:-1px}
  .phone-head{left:30px;top:186px;font-family:var(--head);font-weight:800;color:var(--white);font-size:27px;line-height:1.2}
  .bar{height:21px;font-family:var(--head);font-weight:700;font-size:11px;color:var(--navy);text-transform:uppercase;display:flex;align-items:center;padding-left:28px}
  .bar-white{background:var(--white)}
  .bar-clear{background:rgba(210,210,225,.55);color:var(--white)}
  .hero-text{color:var(--white);font-size:11.5px;line-height:1.33}
  .hero-text p{margin-bottom:8px}
  .info-bar{left:421px;top:514px;width:306px;height:21px;background:var(--navy-deep);clip-path:polygon(4% 0,100% 0,100% 100%,0 100%);color:var(--white);font-size:11.5px;display:flex;align-items:center;padding-left:24px}
  .info-bar b{font-style:italic;margin-left:4px}

  /* services */
  .tab{height:20px;background:var(--tab-gray);color:var(--white);font-family:var(--head);font-weight:700;font-size:11px;display:flex;align-items:center;padding-left:30px;clip-path:polygon(0 0,100% 0,94% 100%,0 100%)}
  .copy{left:30px;width:680px;font-size:11.5px;line-height:1.35;color:var(--text)}
  .desk-phone{left:440px;top:544px;width:275px;height:212px;border-radius:14px;background:linear-gradient(160deg,rgba(210,212,220,.35),rgba(235,236,240,.25))}

  /* fiber */
  .fiber{left:0;top:771px;width:742px;height:110px;background:var(--navy)}
  .fiber-art{left:309px;top:771px;width:433px;height:110px;background:
      linear-gradient(180deg,rgba(0,0,0,0) 35%,rgba(120,200,255,.55) 48%,rgba(255,255,255,.7) 50%,rgba(230,90,200,.45) 56%,rgba(0,0,0,0) 70%),
      linear-gradient(90deg,var(--navy),#3a2f8a 50%,#2a1f70)}
  .fiber-title{left:30px;top:784px;font-family:var(--head);font-weight:800;font-size:21px;color:var(--white)}
  .fiber-text{left:30px;top:814px;color:var(--white);font-size:11.5px;line-height:1.3}
  .fiber-note{left:384px;top:847px;width:345px;color:#dfe0f2;font-size:9.5px;line-height:1.25;font-style:italic}

  /* it services */
  .it-title{left:30px;top:900px;font-family:var(--head);font-weight:800;font-size:21px;color:var(--navy)}
  .it-note{left:350px;top:902px;font-size:9.5px;color:var(--text)}
  .service-list{top:928px;list-style:none;font-size:11.5px;line-height:1.33;color:var(--text)}
  .service-list li::before{content:"• "}

  /* footer */
  .foot-call{left:0;top:1006px;width:260px;height:34px;background:var(--tab-gray);clip-path:polygon(0 0,100% 0,94% 100%,0 100%);color:var(--white);font-family:var(--head);font-weight:700;font-size:14px;display:flex;align-items:center;padding-left:30px}
  .foot-mail{left:246px;top:1006px;width:275px;height:34px;background:var(--navy);clip-path:polygon(6% 0,100% 0,94% 100%,0 100%);color:var(--white);font-size:14px;display:flex;align-items:center;justify-content:center}
  .foot-web{left:575px;top:1006px;height:34px;display:flex;align-items:center;color:var(--navy);font-family:var(--head);font-weight:700;font-size:13.5px}
</style>
</head>
<body>
<div class="brochure">

  <!-- hero -->
  <div class="abs hero"></div>
  <div class="abs hero-photo" role="img" aria-label="Photo of a smiling support agent with a headset working at a computer in an office, a colleague on a call behind him"></div>
  <div class="abs title-panel"></div>
  <h1 class="abs title">
    <span class="big">UNLEASH</span>
    <span class="mid">THE POWER OF LOCAL</span>
    <span class="big">IT SOLUTIONS</span>
  </h1>
  <div class="abs brand">norvix</div>

  <h2 class="abs phone-head">PHONE SERVICES<br>$19.95/MO</h2>

  <div class="abs bar bar-white" style="left:30px;top:263px;width:262px">Telephone Options:</div>
  <div class="abs bar bar-clear" style="left:338px;top:263px;width:265px">Telephone Pricing Options:</div>

  <div class="abs hero-text" style="left:30px;top:293px;width:290px">
    <p>Calvo C23 with three<br>Way audio calling, 2.8" Black &amp; White LCD Display,<br>3 programmable keys, wired headset support, etc.</p>
    <p>Calvo C29 with three<br>Way audio calling, 4.3" Color LCD Display, 10<br>programmable keys, wireless headset support, etc.</p>
  </div>
  <div class="abs hero-text" style="left:363px;top:293px;width:240px">
    Calvo C23 purchase for $75<br>Each or monthly rental of $2.00/mo<br>Calvo C29 purchase for $135<br>Each or monthly rental of $3.50/mo
  </div>

  <div class="abs bar bar-white" style="left:30px;top:411px;width:410px">Business Telephone Features:</div>
  <div class="abs hero-text" style="left:30px;top:443px;width:320px">
    • Caller-ID, Call Forwarding<br>• Simultaneous Ring<br>• Virtual Assistance/Auto Attendant<br>• 1 telephone number per phone included and much more.
  </div>
  <div class="abs hero-text" style="left:350px;top:443px;width:200px">
    • Call Transfer<br>• Mobile App<br>• 1-line per phone included
  </div>

  <div class="abs info-bar">For more information head to <b>www.norvixit.com</b></div>

  <!-- services -->
  <div class="abs desk-phone" role="img" aria-label="Faded photo of the desk IP phone offered with the plan"></div>

  <h3 class="abs tab" style="left:0;top:537px;width:228px">IT Services That Mean Business</h3>
  <p class="abs copy" style="top:564px">Experience fanatical customer service with our affordable, full-service IT solutions. We’re 100% local, ensuring leading response times and personalized support—so you can focus on what you do best.</p>

  <h3 class="abs tab" style="left:0;top:606px;width:330px">Talk More, Worry Less with Our Telephone Services</h3>
  <p class="abs copy" style="top:632px">Say goodbye to overpriced equipment and hello to our free phone plan. Keep your number and enjoy unlimited local and long-distance calling. Tailor your phone system to your business needs and rest assured—our rates are always the lowest in town.</p>

  <h3 class="abs tab" style="left:0;top:672px;width:275px">Highspeed Internet That Sets You Apart</h3>
  <p class="abs copy" style="top:699px">Stay connected with blazing-fast speeds—from 1Gbps to 10Gbps, both up and down. Benefit from a static IP address and unbeatable prices, backed by 100% local support. Get the connectivity your business deserves at the best value in town.</p>

  <p class="abs copy" style="top:750px">Elevate your business with cutting-edge technology.</p>

  <!-- fiber -->
  <div class="abs fiber"></div>
  <div class="abs fiber-art" role="img" aria-label="Abstract image of fast-moving blue, white and pink light streaks suggesting fiber data speed"></div>
  <h2 class="abs fiber-title">HIGH SPEED FIBER INTERNET</h2>
  <div class="abs fiber-text">
    BANDWIDTH OPTIONS:<br>100Mbps starting at $135/mo<br>150Mbps starting at $185/mo<br>*Price varies depending on location
  </div>
  <p class="abs fiber-note">Features/Benefits: Dedicated symmetrical uplink &amp; downlink speeds, no slow down during peak times, 99.99% uptime guarantee, static IP address, local support.</p>

  <!-- it services -->
  <h2 class="abs it-title">IT SERVICES</h2>
  <p class="abs it-note">*STANDARD HOURLY RATE $75/HR OR CUSTOMIZED MONTHLY RATE FOR ALL SERVICES</p>
  <ul class="abs service-list" style="left:30px">
    <li>PC Protection</li><li>Server Protection</li><li>Backups &amp; Disaster Recovery</li><li>Email/Spam Protection</li>
  </ul>
  <ul class="abs service-list" style="left:221px">
    <li>PC &amp; Network Hardware Sales</li><li>Software Sales</li><li>Consulting</li><li>Cloud Services</li>
  </ul>
  <ul class="abs service-list" style="left:410px">
    <li>Ransomware Protection</li><li>Cloud Office Suite</li><li>Troubleshooting/Repair</li><li>WiFi</li>
  </ul>

  <!-- footer -->
  <div class="abs foot-call">Call Us. 555.014.2290</div>
  <div class="abs foot-mail">sales@norvixit.com</div>
  <div class="abs foot-web">www.norvixit.com</div>
</div>
</body>
</html>
```